Menu Board 1000mmx500mm re-design

I would like to re-design exiting menu board 1000mmx500mm. Current board letters are bit to small to read. I would like to have pictures (attached) of the food offered on it and at the same time to create balance between pictures and size of the text to be easily readable. Fonts and colours are up to designer choice but prefer warm and bright colours rather anything dark.

Target Market(s)

Food industry

Industry/Entity Type

Food

Font styles to use
Other font styles liked:
• I leave font choice to designer

Colors
FFC000
F8CF3A
FAE287
FDF2CF
FEFAEE
F0912C
F2A743
F7CA91
FBE8D2
FDF5EE
EE7325
F08F49
F5BC92
FAE3D3
FDF4ED

Requirements
Must have
• Pictures + Text
Nice to have
• Balance between images and text.
Should not have
• Can't think of any

```html
<!DOCTYPE html>
<html lang="en">
<head>
<meta charset="utf-8">
<title>Menu Board</title>
<link href="https://fonts.googleapis.com/css2?family=Montserrat:wght@400;500;700;800&family=Bebas+Neue&display=swap" rel="stylesheet">
<style>
  :root {
    --stage: #d9d9d9;
    --cream: #fcf9f1;
    --orange: #e8562a;
    --orange-light: #f08f49;
    --ink: #1f1f1f;
    --ink-soft: #444;
    --white: #ffffff;
  }
  * { margin: 0; padding: 0; box-sizing: border-box; }
  html, body { width: 1200px; height: 896px; overflow: hidden; }
  body { background: var(--stage); font-family: "Montserrat", sans-serif; color: var(--ink); }

  .menu-board {
    position: absolute; left: 385px; top: 18px;
    width: 430px; height: 860px;
    background: var(--cream); overflow: hidden;
    box-shadow: 0 6px 18px rgba(0,0,0,.18);
  }
  .hero { position: absolute; left: 0; top: 0; width: 430px; height: 380px; }

  .menu-list { position: absolute; left: 0; top: 0; width: 100%; height: 100%; }
  .menu-item { position: absolute; left: 23px; display: flex; align-items: flex-start; }
  .price-badge {
    flex: none; width: 39px; height: 39px; border-radius: 50%;
    background: var(--orange); color: var(--white);
    font-weight: 700; font-size: 14px; letter-spacing: -.5px;
    display: flex; align-items: center; justify-content: center;
    margin-right: 10px;
  }
  .price-badge--small { font-size: 12.5px; }
  .item-text { padding-top: 0; }
  .item-name { font-weight: 800; font-size: 23px; line-height: 1; letter-spacing: .4px; text-transform: uppercase; }
  .item-desc { font-weight: 500; font-size: 15.5px; line-height: 19px; color: var(--ink-soft); margin-top: 3px; }

  .drinks { position: absolute; left: 23px; top: 762px; display: flex; align-items: center; }
  .drinks .item-name { margin-right: 14px; }

  .sauces-bar {
    position: absolute; left: 10px; top: 816px; width: 403px; height: 44px;
    background: var(--orange); border-radius: 22px 22px 0 0;
    display: flex; align-items: center; padding-left: 42px; color: var(--white);
  }
  .sauces-title { font-family: "Bebas Neue", sans-serif; font-size: 31px; line-height: 1; margin-right: 14px; padding-top: 3px; }
  .sauces-list { font-weight: 700; font-size: 13.5px; letter-spacing: .3px; }
</style>
</head>
<body>
<main class="menu-board">
  <svg class="hero" viewBox="0 0 430 380" xmlns="http://www.w3.org/2000/svg">
    <defs>
      <linearGradient id="wrapTones" x1="0" y1="0" x2="1" y2="1">
        <stop offset="0" stop-color="#5a4a3e"/>
        <stop offset=".45" stop-color="#d9b77c"/>
        <stop offset="1" stop-color="#8a6a48"/>
      </linearGradient>
      <radialGradient id="chickenTones"><stop offset="0" stop-color="#e9d9a8"/><stop offset="1" stop-color="#8c5a2c"/></radialGradient>
      <radialGradient id="potatoTones"><stop offset="0" stop-color="#f2b84a"/><stop offset="1" stop-color="#4a3030"/></radialGradient>
      <linearGradient id="sandwichTones" x1="0" y1="0" x2="0" y2="1">
        <stop offset="0" stop-color="#ecebf0"/><stop offset=".4" stop-color="#e0b27a"/><stop offset=".65" stop-color="#5d7d3a"/><stop offset="1" stop-color="#8a5230"/>
      </linearGradient>
      <clipPath id="clipLeft"><circle cx="75" cy="282" r="62"/></clipPath>
    </defs>
    <rect width="430" height="380" fill="url(#wrapTones)" role="img" aria-label="Grilled chicken wraps stacked, filled with greens, tomato and onion"/>
    <path d="M0 318 C130 320 330 300 430 228 L430 380 L0 380 Z" fill="var(--cream)"/>
    <path d="M0 318 C130 320 330 300 430 228" fill="none" stroke="var(--orange-light)" stroke-width="8"/>
    <circle cx="75" cy="282" r="64" fill="var(--orange)"/>
    <circle cx="75" cy="282" r="61" fill="url(#chickenTones)" role="img" aria-label="Roast chicken leg with vegetable rice"/>
    <circle cx="319" cy="267" r="63" fill="var(--orange)"/>
    <circle cx="319" cy="267" r="60" fill="url(#sandwichTones)" role="img" aria-label="Ciabatta sandwich with chicken and rocket"/>
    <circle cx="188" cy="267" r="81" fill="var(--orange)"/>
    <circle cx="188" cy="267" r="77" fill="var(--white)"/>
    <circle cx="188" cy="267" r="74" fill="url(#potatoTones)" role="img" aria-label="Roasted potatoes with thyme and garlic"/>
  </svg>

  <section class="menu-list">
    <div class="menu-item" style="top:362px">
      <span class="price-badge">£6</span>
      <div class="item-text">
        <h2 class="item-name">Ciabatta</h2>
        <p class="item-desc">Roti Chicken, Rucola, Caramelized<br>Onions, Tomato, Fresh Onion</p>
      </div>
    </div>
    <div class="menu-item" style="top:437px">
      <span class="price-badge">£7</span>
      <div class="item-text">
        <h2 class="item-name">Wrap</h2>
        <p class="item-desc">Roti Chicken, Crunchy Slaw, Tomato,<br>Fresh Onion &amp; Sauce of your choice</p>
      </div>
    </div>
    <div class="menu-item" style="top:513px">
      <span class="price-badge">£8</span>
      <div class="item-text">
        <h2 class="item-name">Beetroot Wrap</h2>
        <p class="item-desc">Roti Chicken, Crunchy Slaw, Tomato,<br>Fresh Onion &amp; Sauce of your choice</p>
      </div>
    </div>
    <div class="menu-item" style="top:594px">
      <span class="price-badge">£9</span>
      <div class="item-text">
        <h2 class="item-name">1/4 Chicken Box</h2>
        <p class="item-desc">Roti Chicken, Veggie Rice &amp; Salad</p>
      </div>
    </div>
    <div class="menu-item" style="top:655px">
      <span class="price-badge">£14</span>
      <div class="item-text">
        <h2 class="item-name">1/2 Chicken Box</h2>
        <p class="item-desc">Roti Chicken, Veggie Rice &amp; Salad</p>
      </div>
    </div>
    <div class="menu-item" style="top:710px">
      <span class="price-badge price-badge--small">£2.5</span>
      <div class="item-text">
        <h2 class="item-name">Roasted Potatoes</h2>
        <p class="item-desc">Thyme &amp; Garlic</p>
      </div>
    </div>
    <div class="drinks">
      <span class="price-badge">£1</span>
      <h2 class="item-name">Water</h2>
      <span class="price-badge price-badge--small">£1.8</span>
      <h2 class="item-name">Can &amp; Juices</h2>
    </div>
  </section>

  <footer class="sauces-bar">
    <span class="sauces-title">SAUCES</span>
    <span class="sauces-list">BBQ, PIRI PIRI, GARLIC, MAYO</span>
  </footer>
</main>
</body>
</html>
```